Derek Mavlow Business card

Hey there, I’m hoping to have a business card designed. I’m in Real estate and just switched to a new Brokerage called: The Property Quarter

The back could just be the company name maybe or whatever looks good!

I’ve attached some logos of our company and some cards my buddy had done up.

On the card:
Derek Mavlow
derekmavlow@postnest.example
587-204-6618
derekmavlow-homes.example

Target Market(s)

Home buyers and sellers

Industry/Entity Type

Real Estate

Contact Information for Business Card

just looking for a cool and modern design with my picture on it. I like the idea of Black and red being used.

Requirements
Must have
• all the details provided. I'm open to anything. Just want a professional looking card.

```html
<!DOCTYPE html>
<html lang="en">
<head>
<meta charset="utf-8">
<title>Derek Mavlow – Business Card</title>
<link href="https://fonts.googleapis.com/css2?family=Poppins:wght@400;500;700&display=swap" rel="stylesheet">
<style>
  :root {
    --canvas: #2b2b2c;
    --card: #060607;
    --red: #e0193a;
    --white: #f4f4f4;
    --faint: #2e2e30;
    --photo-dark: #0b0b0c;
    --photo-mid: #2a2a2d;
  }
  * { box-sizing: border-box; margin: 0; padding: 0; }
  html, body {
    width: 1200px; height: 689px; overflow: hidden;
    background: var(--canvas);
    font-family: "Poppins", sans-serif;
  }
  .canvas {
    width: 1200px; height: 689px;
    display: flex; align-items: center; justify-content: center; gap: 40px;
  }
  .card {
    position: relative;
    width: 540px; height: 309px;
    background: var(--card);
    border: 2px solid var(--red);
    border-radius: 22px;
    overflow: hidden;
  }
  /* Back */
  .card--back { display: flex; align-items: center; justify-content: center; }
  .back-name {
    font-weight: 700; font-size: 40px; letter-spacing: 1px;
    text-transform: uppercase; color: var(--faint);
    text-align: center; line-height: 1.1;
  }
  /* Front */
  .portrait {
    position: absolute; left: 24px; bottom: 0;
    width: 240px; height: 270px;
    border-radius: 120px 120px 0 0;
    background: radial-gradient(ellipse at 50% 35%, var(--photo-mid), var(--photo-dark) 70%);
  }
  .info {
    position: absolute; left: 286px; top: 54px; right: 20px;
  }
  .brand {
    font-weight: 700; font-size: 22px; line-height: 1.1;
    color: var(--white); text-transform: uppercase;
  }
  .agent-name {
    margin-top: 26px;
    font-weight: 500; font-size: 21px; letter-spacing: 0.5px;
    color: var(--red); text-transform: uppercase;
  }
  .contact { list-style: none; margin-top: 14px; }
  .contact li {
    display: flex; align-items: center; gap: 9px;
    font-size: 12.5px; color: var(--white); margin-bottom: 8px;
    white-space: nowrap;
  }
  .contact svg { width: 15px; height: 15px; flex: none; }
</style>
</head>
<body>
<main class="canvas">
  <section class="card card--back">
    <p class="back-name">The Property<br>Quarter</p>
  </section>

  <section class="card card--front">
    <div class="portrait" role="img" aria-label="Portrait photo of Derek Mavlow in a dark suit, leaning on his arms"></div>
    <div class="info">
      <p class="brand">The Property Quarter</p>
      <h1 class="agent-name">Derek Mavlow</h1>
      <ul class="contact">
        <li>
          <svg viewBox="0 0 24 24" aria-hidden="true"><path fill="var(--red)" d="M6.6 10.8a15.1 15.1 0 0 0 6.6 6.6l2.2-2.2c.3-.3.7-.4 1-.2 1.1.4 2.3.6 3.6.6.6 0 1 .4 1 1V20c0 .6-.4 1-1 1A17 17 0 0 1 3 4c0-.6.4-1 1-1h3.5c.6 0 1 .4 1 1 0 1.3.2 2.5.6 3.6.1.3 0 .7-.2 1z"/></svg>
          587-204-6618
        </li>
        <li>
          <svg viewBox="0 0 24 24" aria-hidden="true"><rect x="2" y="5" width="20" height="14" rx="1.5" fill="var(--red)"/><path d="M3 6l9 7 9-7" fill="none" stroke="var(--card)" stroke-width="1.6"/></svg>
          derekmavlow@postnest.example
        </li>
        <li>
          <svg viewBox="0 0 24 24" aria-hidden="true"><g fill="none" stroke="var(--red)" stroke-width="1.8"><circle cx="12" cy="12" r="9.5"/><ellipse cx="12" cy="12" rx="4" ry="9.5"/><path d="M2.5 12h19M4 7h16M4 17h16"/></g></svg>
          derekmavlow-homes.example
        </li>
      </ul>
    </div>
  </section>
</main>
</body>
</html>
```